Stationery Design Project

We need a stationery design package for a new company based in Luxembourg called "Morvesta Tax & Consulting" with a legal name "Morvesta S.a.r.l.".

We are a personal tax compliance and consulting company specialising in Luxembourg, UK and US taxation.

We require a stationery package including the following:-

- letterhead/paper
- envelopes (C4, C5, DL)
- compliments slip
- business cards
- folder (A4 with two pockets)

We are looking for a modern, elegant design which remains professional.
Updates

Hi everyone, thank you for the designs so far - there are some that we do like so I have changed the status to non-refundable as we will definitely take one of them forwards.

I have today received the final logo files from the website designer so I will upload these shortly.  We are reviewing the designs to date tonight so will provide further feedback latest tomorrow morning.

Thanks again
Greta

Industry/Entity Type

Business

Requirements
Must have
• The design should focus on the following main colour:-
#7D1935
and could use these two colours as accents, if required:-
#4A96AD
#F5F3EE

We have uploaded our logo which has been finalised 31 July 2013 (note I have deleted the previous logo files that were uploaded). I have uploaded jpg, png, psd files. I also have tif and eps but these are large in size so have not uploaded here - if you need them please let me know and I can upload.
Nice to have
• Business cards - we would like the business cards to be full main colour on one side. We are considering using a QR code on the business card to link to the website, but not a necessity.

Folder - we are considering including the company contact information preprinted on the inside right pocket instead of business cards

```html
<!DOCTYPE html>
<html lang="en">
<head>
<meta charset="utf-8">
<title>Morvesta Tax &amp; Consulting — Business Card</title>
<link href="https://fonts.googleapis.com/css2?family=Mulish:wght@400;700&display=swap" rel="stylesheet">
<style>
  :root {
    --brand: #7d1935;
    --brand-light: #9e3a62;
    --paper: #f5f3ee;
    --card-white: #f4f4f4;
    --ink: #3c3c3c;
    --ink-soft: #5a5a5a;
    --stage: #e3e3e3;
    --ring: #b8b8b8;
    --faint-ring: #dcdcdc;
    --faint-fill: #ecd9e0;
  }
  * { box-sizing: border-box; margin: 0; padding: 0; }
  html, body {
    width: 1200px; height: 900px; overflow: hidden;
    background: var(--stage);
    font-family: "Mulish", "Century Gothic", sans-serif;
  }
  .stage { position: relative; width: 1200px; height: 900px; }
  .card {
    position: absolute; width: 560px; height: 320px;
    box-shadow: 0 10px 28px rgba(0,0,0,0.22);
    overflow: hidden;
  }
  /* Front */
  .card-front {
    left: 110px; top: 90px;
    background: linear-gradient(135deg, var(--brand) 0%, var(--brand-light) 100%);
    color: #fff;
  }
  .brand-lockup { position: absolute; display: flex; align-items: center; gap: 14px; }
  .brand-mark {
    width: 56px; height: 56px; border-radius: 50%;
    border: 2px solid currentColor; flex: none;
  }
  .brand-name { font-weight: 400; font-size: 24px; letter-spacing: 1px; line-height: 1; }
  .card-front .brand-lockup { left: 60px; top: 110px; color: #fff; }
  .website {
    position: absolute; right: 40px; top: 150px;
    font-size: 12px; letter-spacing: 2.5px;
  }
  /* Back */
  .card-back {
    left: 530px; top: 480px;
    background: var(--card-white);
    color: var(--ink);
  }
  .back-decor { position: absolute; left: -60px; top: 20px; }
  .card-back .brand-lockup { left: 190px; top: 40px; }
  .card-back .brand-mark { border-color: var(--ring); }
  .card-back .brand-name { color: var(--brand); font-size: 22px; }
  .holder { position: absolute; left: 340px; top: 140px; }
  .holder-name { font-weight: 700; font-size: 15px; letter-spacing: 0.5px; color: var(--ink); }
  .holder-role { font-size: 13px; color: var(--ink-soft); margin-top: 2px; }
  .contact { position: absolute; left: 40px; bottom: 30px; font-size: 13px; line-height: 1.45; color: var(--ink-soft); }
  .contact b { color: var(--ink); font-weight: 700; }
  .contact .address { margin-top: 8px; }
</style>
</head>
<body>
<main class="stage">
  <section class="card card-front" aria-label="Business card front">
    <div class="brand-lockup">
      <span class="brand-mark"></span>
      <span class="brand-name">Morvesta Tax &amp; Consulting</span>
    </div>
    <div class="website">www.morvesta.lu</div>
  </section>

  <section class="card card-back" aria-label="Business card back">
    <svg class="back-decor" width="360" height="360" viewBox="0 0 360 360" aria-hidden="true">
      <circle cx="180" cy="180" r="160" fill="var(--faint-fill)" opacity="0.45"/>
      <circle cx="180" cy="180" r="170" fill="none" stroke="var(--faint-ring)" stroke-width="3"/>
    </svg>
    <div class="brand-lockup">
      <span class="brand-mark"></span>
      <span class="brand-name">Morvesta Tax &amp; Consulting</span>
    </div>
    <div class="holder">
      <div class="holder-name">ELIN HARWOOD</div>
      <div class="holder-role">Director</div>
    </div>
    <div class="contact">
      <div><b>Tel:</b> +352 26 48 1200</div>
      <div><b>Mob:</b> +352 621 48 1299</div>
      <div><b>Email:</b> harwood@morvesta.lu</div>
      <div class="address">14 Rue Beaumont<br>L-1219 Luxembourg</div>
    </div>
  </section>
</main>
</body>
</html>
```